Tri-fold Brochure Design for Law Firm

I need a tri-fold brochure to give to prospective clients.
I have attached a Photoshop design file of a tri-fold brochure. The content (copy) is good, however, he brochure itself looks very amateurish.
I want a professional, sophisticated looking brochure.
The law firm specializes in commercial debt collection.
The law firm is located in New York City.
Our target market is business owners, doctors, lawyers, collection agencies and accountants.
Visit my website which is being designed at www.dorvenlaw.com. I like the font used for the name of my company and the rich blue color used.

Target Market(s)

Business Owners, Doctors, Law Firms and Accountants

Industry/Entity Type

Law Firm

Font styles to use
Serif

Requirements
Must have
• Professional quality graphic work. Attention to details.
• PHOTOGRAPHS ONLY, NO CLIP-ART.
• DARK COLORS - NAVY BLUE, HUNTER GREEN, BLACK, GRAY & WHITE
Nice to have
• I want it to look smart, modern and sophisticated.
• Visit my website which is being designed at www.dorvenlaw.com. I like the font used for the name of my company and the rich blue color used.
Should not have
• Bad artwork
• CLIP ART

```html
<!DOCTYPE html>
<html lang="en">
<head>
<meta charset="utf-8">
<title>Marcus Dorven &amp; Company, PLLC – Tri-fold Brochure</title>
<link rel="stylesheet" href="https://fonts.googleapis.com/css2?family=Bebas+Neue&family=Oswald:wght@500;600&family=Lato:wght@400;700&display=swap">
<style>
:root{
  --navy:#1b2d5b;
  --navy-deep:#15244c;
  --sky:#1a9be0;
  --rule:#2f6db3;
  --ink:#1e1e1e;
  --paper:#ffffff;
  --page:#e6e6e6;
  --gray:#b9bcc2;
}
*{margin:0;padding:0;box-sizing:border-box}
html,body{width:1200px;height:1200px;overflow:hidden;background:var(--page)}
.brochure{position:absolute;left:0;top:133px;width:1200px;height:933px;background:var(--paper);overflow:hidden;font-family:"Lato",sans-serif;color:var(--ink)}
.panel{position:absolute;top:0;height:892px}
.panel-about{left:0;width:398px;background:linear-gradient(90deg,#ffffff 0%,#f1f3f6 60%,#e9ecf0 100%)}
.panel-contact{left:398px;width:394px;background:var(--navy)}
.panel-cover{left:792px;width:408px;background:#fbfbfb}
.tag{position:absolute;left:0;height:25px;padding:0 38px 0 22px;background:var(--sky);color:#fff;font-family:"Oswald",sans-serif;font-weight:500;font-size:12.5px;line-height:25px;border-radius:0 13px 13px 0;letter-spacing:.2px}
.copy{position:absolute;left:22px;width:359px;font-size:14px;line-height:20.8px}
.copy p{margin-bottom:17px}
.justify{text-align:justify}
.serve-title{font-weight:700;margin-bottom:15px!important}
.serve-list{list-style:none}
.serve-list li{line-height:22.3px;padding-left:12px;position:relative}
.serve-list li::before{content:"";position:absolute;left:1px;top:10px;width:4px;height:4px;border-radius:50%;background:var(--ink)}
.why p{margin-bottom:6px;line-height:18px}
.contact-block{position:absolute;left:50px;width:294px;text-align:center;color:#fff}
.contact-block h2,.contact-block h3{font-family:"Oswald",sans-serif;font-weight:600;font-size:15px;line-height:20px;letter-spacing:.1px}
.contact-block .sub{font-family:"Oswald",sans-serif;font-weight:500;font-size:11.5px;line-height:18px}
.contact-block p{font-size:15px;line-height:24px}
.contact-block .strong{font-weight:700;font-size:13.5px;line-height:18px}
.rule{position:absolute;left:50px;width:294px;height:1px;background:var(--rule)}
.ico{display:inline-block;width:12px;height:11px;margin-right:6px;vertical-align:-1px}
.photo{position:absolute}
.cover-title{position:absolute;left:44px;top:650px;font-family:"Bebas Neue",sans-serif;font-size:66px;line-height:62px;color:var(--navy);letter-spacing:.5px}
.cover-sub{position:absolute;left:46px;top:797px;font-family:"Bebas Neue",sans-serif;font-size:35px;color:var(--sky);letter-spacing:.3px}
.footer{position:absolute;left:0;top:892px;width:1200px;height:41px;background:var(--navy);color:var(--sky);font-size:19px;line-height:41px}
.footer span{position:absolute;top:0;transform:translateX(-50%);white-space:nowrap}
.footer svg{width:18px;height:18px;vertical-align:-3px;margin-right:9px}
</style>
</head>
<body>
<main class="brochure">

  <section class="panel panel-about">
    <div class="tag" style="top:24px">A TRUSTED PARTNER</div>
    <div class="copy" style="top:63px">
      <p class="justify">We under the business of debt collection. Our primary focus is to help our clients secure the payments they are owed. We work closely with both private clients and leading service professionals, such as attorneys and accountants, to provide added value to their clients through customized debt collection services.</p>
      <p>We value our relationships as trusted advisors.</p>
      <p class="serve-title">We proudly serve:</p>
      <ul class="serve-list">
        <li>Law firms</li>
        <li>Accounting Firms</li>
        <li>Manufacturers</li>
        <li>Wholesalers and Distributors</li>
        <li>Collection Agencies</li>
        <li>Financial Service Companies</li>
        <li>Factors</li>
        <li>Doctors and Healthcare Professionals</li>
        <li>Carting Companies</li>
        <li>Oil Companies</li>
        <li>Freight Forwarders &amp; Custom Brokers</li>
        <li>Publishing and Advertising Companies</li>
        <li>Construction and Real Estate Firms</li>
      </ul>
    </div>
    <div class="tag" style="top:625px">WHY USE US</div>
    <div class="copy why" style="top:664px">
      <p style="margin-bottom:9px">Anyone can sue a Debtor.</p>
      <p>It’s not difficult to get nasty or to treat people who owe you money in a rude and unprofessional way.</p>
      <p class="justify">However, very few people have the skill, temperament and experience needed to effectively negotiate with Debtors, stakeholders, lawyers, as well as, court personnel, sheriffs and bankers to efficiently collect the most money possible in the least amount of time.</p>
      <p>We truly understand the nature of commercial debt.</p>
      <p>Collecting money is a specialized skill.</p>
    </div>
  </section>

  <section class="panel panel-contact">
    <div class="contact-block" style="top:30px">
      <h2>MARCUS DORVEN &amp; COMPANY, PLLC</h2>
      <div class="sub">DEBT COLLECTION ATTORNEYS IN NEW YORK STATE</div>
      <p style="font-weight:700;font-size:14px;line-height:22px"><svg class="ico" viewBox="0 0 12 12"><circle cx="6" cy="6" r="5.5" fill="#1a9be0"/></svg>www.DorvenLaw.com</p>
    </div>
    <div class="rule" style="top:106px"></div>
    <div class="contact-block" style="top:132px">
      <h3>MARCUS T. DORVEN, ESQUIRE</h3>
      <p style="line-height:21px">President</p>
      <p style="line-height:23px"><svg class="ico" viewBox="0 0 12 11"><rect x="0.5" y="1.5" width="11" height="8.5" fill="#1a9be0"/><path d="M0.5 1.5 L6 6 L11.5 1.5" stroke="#1b2d5b" fill="none"/></svg>mdorven@dorvenlaw.com</p>
      <p><svg class="ico" viewBox="0 0 12 11"><rect x="0" y="1" width="12" height="9" rx="1" fill="#1a9be0"/><rect x="3" y="3" width="6" height="5" fill="#1b2d5b"/></svg>(212) 555-0147</p>
    </div>
    <div class="rule" style="top:237px"></div>
    <div class="contact-block" style="top:257px">
      <h3 style="margin-bottom:5px">HARLOW COUNTY OFFICE</h3>
      <p>318 RIDGEVIEW AVENUE, SUITE 104</p>
      <p>HARLOW PLAINS, NEW YORK 10690</p>
      <p style="line-height:20px">(Off Exit 4, on EB Route 90)</p>
    </div>
    <div class="rule" style="top:368px"></div>
    <div class="contact-block" style="top:384px">
      <h3 style="margin-bottom:6px">MAILING ADDRESS</h3>
      <p style="line-height:18px">145 LINDEN AVENUE SOUTH, SUITE 2210</p>
      <p style="line-height:18px;margin-bottom:14px">NEW YORK, NEW YORK 10099-1544</p>
      <p class="strong"><svg class="ico" viewBox="0 0 12 11"><rect x="0" y="1" width="12" height="9" rx="1" fill="#1a9be0"/><rect x="3" y="3" width="6" height="5" fill="#1b2d5b"/></svg>(877) 555-0190 (TOLL FREE)</p>
      <p class="strong"><svg class="ico" viewBox="0 0 12 11"><rect x="0" y="1" width="12" height="9" rx="1" fill="#1a9be0"/><rect x="3" y="3" width="6" height="5" fill="#1b2d5b"/></svg>(212) 555-0183</p>
      <p class="strong"><svg class="ico" viewBox="0 0 12 11"><path d="M1 3 Q6 -1 11 3 L9 5 L3 5 Z" fill="#1a9be0"/><rect x="3" y="6" width="6" height="4" fill="#1a9be0"/></svg>(917) 555-0126</p>
    </div>
    <div class="rule" style="top:539px"></div>

    <svg class="photo" style="left:0;top:560px" width="394" height="332" viewBox="0 0 394 332" role="img" aria-label="Photograph of a domed capitol building with columned wings, in black and white">
      <defs>
        <linearGradient id="capitolTone" x1="0" y1="0" x2="0" y2="1">
          <stop offset="0" stop-color="#f2f2f2"/>
          <stop offset="0.55" stop-color="#c9c9c9"/>
          <stop offset="1" stop-color="#7d7d7d"/>
        </linearGradient>
      </defs>
      <rect width="394" height="332" fill="url(#capitolTone)"/>
      <path d="M0 0 H394 V20 Q200 10 0 95 Z" fill="#1b2d5b"/>
      <path d="M0 95 Q200 10 394 20 V26 Q210 24 0 118 Z" fill="#1a9be0"/>
      <path d="M0 118 Q210 24 394 26 V36 Q220 40 0 135 Z" fill="#c2c5cb"/>
    </svg>
  </section>

  <section class="panel panel-cover">
    <svg class="photo" style="left:0;top:0" width="408" height="620" viewBox="0 0 408 620" role="img" aria-label="Photograph of a columned courthouse under blue sky with a flag on a pole">
      <defs>
        <linearGradient id="courtTone" x1="0" y1="0" x2="0" y2="1">
          <stop offset="0" stop-color="#9fcbed"/>
          <stop offset="0.45" stop-color="#c9dbe8"/>
          <stop offset="0.7" stop-color="#e2e2dc"/>
          <stop offset="1" stop-color="#a9aca3"/>
        </linearGradient>
      </defs>
      <rect width="408" height="620" fill="url(#courtTone)"/>
      <path d="M0 0 H408 V0 Q150 -5 0 110 Z" fill="#fbfbfb"/>
      <path d="M0 95 Q150 5 395 0 Q160 22 0 120 Z" fill="#1b2d5b"/>
      <path d="M0 580 Q260 590 408 480 V620 H0 Z" fill="#fbfbfb"/>
      <path d="M0 570 Q250 580 408 480 V520 Q260 600 0 590 Z" fill="#c2c5cb"/>
      <path d="M0 574 Q250 574 408 490 V510 Q250 590 0 585 Z" fill="#1a9be0"/>
      <path d="M0 568 Q250 566 408 478 V496 Q250 578 0 578 Z" fill="#1b2d5b"/>
    </svg>
    <h1 class="cover-title">MARCUS DORVEN<br>&amp; COMPANY, PLLC</h1>
    <div class="cover-sub">DEBT COLLECTION ATTORNEYS</div>
  </section>

  <footer class="footer">
    <span style="left:200px"><svg viewBox="0 0 18 18"><path d="M3 1.5 L6.5 1.5 L8 5.5 L6 7 Q7.5 10.5 11 12 L12.5 10 L16.5 11.5 V15 Q16.5 16.5 15 16.5 Q2 15.5 1.5 3 Q1.5 1.5 3 1.5 Z" fill="#1a9be0"/></svg>(877) 555-0190</span>
    <span style="left:600px">www.dorvenlaw.com</span>
    <span style="left:997px"><svg viewBox="0 0 18 18"><path d="M3 1.5 L6.5 1.5 L8 5.5 L6 7 Q7.5 10.5 11 12 L12.5 10 L16.5 11.5 V15 Q16.5 16.5 15 16.5 Q2 15.5 1.5 3 Q1.5 1.5 3 1.5 Z" fill="#1a9be0"/></svg>(877) 555-0190</span>
  </footer>

</main>
</body>
</html>
```